Simple templates for management consulting firm

Vireo Advisors is a management consulting firm based in the DC area. We have all the basic templates but would like to tweak them so they look consistent.

Check us out at www.vireoadvisors-example.com

For this project we would like to get
a tweaked powerpoint template (header should be up)
a letter template for letters
a fax template

Current templates and our logo are attached.
Updates

We just increased the budget of this project.

We got questions about the project. Here are our thoughts on this one:

Please include the logo into the fax template. If you find improvements in the layout then feel free to make those. Let's not overthink this too much. Keep it simple :)

We like The powerpoint concept as is. The slide titles are for some reasons on the bottom. It seems to irritate some folks. If you can switch the slide titles to the top, keep the look and feel of the slides and work in the logo then that would be fantastic.

The letter head should include the following

Vireo Advisors, LLC Box 5817, Pine Hollow, VA 20499 Phone 555 814-2906, Fax 555 276 9143, www.vireoadvisors-example.com and the logo.

Again, let's keep it simple.

Thank you for considering this project.

We just realize that we are not necessarily inisting to use the red in the slides.
Any approach that would work with the logo will be considered.

Thanks for your creativity.

Target Market(s)

tech companies, Meridian 400, venture capitalists

Industry/Entity Type

Management Consulting

Requirements
Must have
• Keep it simple please

```html
<!DOCTYPE html>
<html lang="en">
<head>
<meta charset="utf-8">
<title>Vireo Advisors Stationery</title>
<link href="https://fonts.googleapis.com/css2?family=Source+Sans+3:wght@400;600&display=swap" rel="stylesheet">
<style>
  :root {
    --backdrop: #ffffff;
    --paper: #efedea;
    --brand-red: #a81e22;
    --charcoal: #454342;
    --gold: #d3a13f;
    --silver: #b3b1ae;
    --white: #ffffff;
    --window: #f6f5f3;
    --window-edge: #dcd9d4;
  }
  html, body {
    margin: 0;
    padding: 0;
    width: 1200px;
    height: 900px;
    overflow: hidden;
    background: var(--backdrop);
    font-family: "Source Sans 3", Arial, sans-serif;
  }
  .canvas {
    position: relative;
    width: 1200px;
    height: 900px;
  }

  /* Letterhead */
  .letterhead {
    position: absolute;
    left: 49px;
    top: 64px;
    width: 582px;
    height: 748px;
    background: var(--paper);
  }
  .letterhead__header {
    position: absolute;
    left: 0;
    top: 0;
    width: 100%;
    height: 57px;
    background: var(--brand-red);
  }
  .brand {
    position: absolute;
    display: flex;
    align-items: center;
    gap: 6px;
    font-weight: 600;
    white-space: nowrap;
  }
  .brand__dot {
    border-radius: 50%;
    flex: none;
  }
  .letterhead .brand {
    left: 28px;
    top: 17px;
    font-size: 17px;
    color: var(--white);
  }
  .letterhead .brand__dot {
    width: 22px;
    height: 22px;
    background: var(--silver);
  }
  .contact {
    position: absolute;
    right: 15px;
    top: 12px;
    text-align: left;
    font-size: 7.5px;
    line-height: 10px;
    color: var(--white);
  }
  .contact__web {
    position: absolute;
    right: 15px;
    top: 44px;
    font-size: 7.5px;
    color: var(--white);
  }
  .letterhead__footer {
    position: absolute;
    left: 0;
    bottom: 0;
    width: 100%;
    height: 53px;
    background: var(--charcoal);
  }
  .address {
    position: absolute;
    left: 13px;
    top: 21px;
    font-size: 7.5px;
    line-height: 10px;
    color: var(--white);
  }
  .address__name {
    color: var(--gold);
  }
  .footer-mark {
    position: absolute;
    right: 16px;
    top: 21px;
    width: 20px;
    height: 20px;
    border-radius: 50%;
    background: var(--silver);
  }

  /* Envelope */
  .envelope {
    position: absolute;
    left: 491px;
    top: 337px;
    width: 657px;
    height: 291px;
    background: var(--paper);
    overflow: hidden;
  }
  .envelope__spine {
    position: absolute;
    left: 0;
    top: 0;
    width: 20px;
    height: 100%;
    background: var(--charcoal);
    border-right: 2px solid var(--gold);
  }
  .envelope .brand {
    left: 33px;
    top: 12px;
    font-size: 22px;
    color: var(--silver);
    gap: 8px;
  }
  .envelope .brand__dot {
    width: 44px;
    height: 44px;
    background: var(--gold);
  }
  .envelope__window {
    position: absolute;
    left: 52px;
    top: 186px;
    width: 233px;
    height: 64px;
    border-radius: 12px;
    background: var(--window);
    border: 1px solid var(--window-edge);
    box-sizing: border-box;
  }
  .envelope__accent {
    position: absolute;
    right: -10px;
    bottom: -38px;
    width: 160px;
    height: 160px;
    border-radius: 50%;
    background: var(--silver);
  }
</style>
</head>
<body>
<main class="canvas">

  <section class="letterhead" aria-label="Letterhead">
    <header class="letterhead__header">
      <div class="brand">
        <span class="brand__dot"></span>
        <span class="brand__name">Vireo Advisors</span>
      </div>
      <div class="contact">
        T: +1 555 814 2906<br>
        F: +1 555 276 9143
      </div>
      <div class="contact__web">www.vireoadvisors-example.com</div>
    </header>
    <footer class="letterhead__footer">
      <div class="address">
        <span class="address__name">Vireo Advisors</span><br>
        LLC Box 5817, Pine Hollow, VA 20499
      </div>
      <span class="footer-mark"></span>
    </footer>
  </section>

  <section class="envelope" aria-label="Window envelope">
    <div class="envelope__spine"></div>
    <div class="brand">
      <span class="brand__dot"></span>
      <span class="brand__name">Vireo Advisors</span>
    </div>
    <div class="envelope__window"></div>
    <div class="envelope__accent"></div>
  </section>

</main>
</body>
</html>
```